Need DL Flyer for Real Estate Drops

We need a real estate flyer ,double sided. With content on 1 side like: Want to know what's your house is worth " contact us today and on other side agent details. We are looking for an ongoing partnership with designer so this assignment will be ongoing

```html
<!DOCTYPE html>
<html lang="en">
<head>
<meta charset="utf-8">
<title>Meridian Realty – DL Flyer</title>
<link rel="stylesheet" href="https://fonts.googleapis.com/css2?family=Baloo+2:wght@400;500;600;700;800&display=swap">
<style>
  :root {
    --red-dark: #a50812;
    --red: #e8222e;
    --navy: #0a1128;
    --yellow: #ffb800;
    --white: #ffffff;
    --paper: #f1f1f1;
    --portrait: #77706d;
  }
  html, body {
    margin: 0;
    width: 1200px;
    height: 1200px;
    overflow: hidden;
    background: var(--paper);
    font-family: "Baloo 2", sans-serif;
  }
  .flyer {
    position: absolute;
    top: 183px;
    width: 393px;
    height: 834px;
    display: block;
  }
  .flyer--front { left: 153px; }
  .flyer--back { left: 654px; }
  .flyer text { font-family: "Baloo 2", sans-serif; }
  .brand-name { font-weight: 500; font-size: 38px; }
  .brand-name--light { fill: var(--white); }
  .headline-strong { fill: var(--white); font-weight: 800; font-size: 54px; }
  .headline-light { fill: var(--white); font-weight: 400; font-size: 40px; }
  .headline-house { fill: var(--yellow); font-weight: 800; font-size: 138px; letter-spacing: -2px; }
  .headline-worth { fill: var(--white); font-weight: 800; font-size: 54px; letter-spacing: 1px; }
  .cta { fill: var(--white); font-weight: 700; font-size: 54px; }
  .cta-phone { fill: var(--white); font-weight: 600; font-size: 44px; letter-spacing: 1px; }
  .tagline { fill: var(--white); font-weight: 700; font-size: 50px; }
  .agent-name { fill: var(--yellow); font-weight: 600; font-size: 42px; }
  .agent-role { fill: var(--white); font-weight: 400; font-size: 19px; }
  .contact { fill: var(--white); font-weight: 400; font-size: 20px; letter-spacing: 0.5px; }
</style>
</head>
<body>

<!-- Front side -->
<svg class="flyer flyer--front" viewBox="0 0 633 1343" xmlns="http://www.w3.org/2000/svg">
  <defs>
    <linearGradient id="front-red" x1="0" y1="0" x2="1" y2="0.3">
      <stop offset="0" stop-color="var(--red-dark)"/>
      <stop offset="1" stop-color="var(--red)"/>
    </linearGradient>
    <linearGradient id="front-red-bottom" x1="0" y1="1" x2="1" y2="0">
      <stop offset="0" stop-color="var(--red-dark)"/>
      <stop offset="0.6" stop-color="var(--red)"/>
    </linearGradient>
    <linearGradient id="photo-main-tone" x1="0" y1="0" x2="0" y2="1">
      <stop offset="0" stop-color="#cbb0e0"/>
      <stop offset="0.45" stop-color="#b58f92"/>
      <stop offset="0.75" stop-color="#7a6a58"/>
      <stop offset="1" stop-color="#8d6660"/>
    </linearGradient>
    <linearGradient id="photo-side-tone" x1="0" y1="0" x2="0" y2="1">
      <stop offset="0" stop-color="#a8b4d8"/>
      <stop offset="0.45" stop-color="#d8c8b4"/>
      <stop offset="0.8" stop-color="#b88a64"/>
      <stop offset="1" stop-color="#6f8a48"/>
    </linearGradient>
    <clipPath id="upper-half"><rect x="-200" y="0" width="900" height="520"/></clipPath>
    <clipPath id="lower-half"><rect x="-200" y="520" width="900" height="900"/></clipPath>
  </defs>

  <rect class="flyer-bg" width="633" height="1343" fill="url(#front-red)"/>
  <path class="navy-panel" d="M0 700 L633 560 L633 1239 L0 1239 Z" fill="var(--navy)"/>
  <path class="red-corner" d="M0 916 L300 1216 Q322 1239 355 1239 L633 1239 L633 1343 L0 1343 Z" fill="url(#front-red-bottom)"/>

  <g class="photo-outline">
    <rect x="-113.5" y="252.5" width="535" height="535" rx="95" fill="none" stroke="var(--yellow)" stroke-width="10" stroke-dasharray="26 18" stroke-linecap="round" transform="rotate(45 154 520)" clip-path="url(#upper-half)"/>
    <rect x="-113.5" y="252.5" width="535" height="535" rx="95" fill="none" stroke="var(--yellow)" stroke-width="10" transform="rotate(45 154 520)" clip-path="url(#lower-half)"/>
  </g>
  <rect class="photo photo--side" role="img" aria-label="Photo of a two-storey suburban house with garden" x="-82" y="284" width="472" height="472" rx="72" fill="url(#photo-side-tone)" transform="rotate(45 154 520)"/>

  <rect class="photo-frame" x="177" y="139" width="518" height="518" rx="88" fill="var(--white)" transform="rotate(45 436 398)"/>
  <rect class="photo photo--main" role="img" aria-label="Photo of a brick single-storey house with garage and front lawn" x="198.5" y="160.5" width="475" height="475" rx="66" fill="url(#photo-main-tone)" transform="rotate(45 436 398)"/>

  <g class="brand">
    <rect x="45" y="38" width="50" height="50" rx="6" fill="var(--white)"/>
    <text class="brand-name brand-name--light" x="106" y="76">meridian</text>
  </g>

  <g class="headline" text-anchor="end">
    <text class="headline-strong" x="605" y="922">want to know</text>
    <text class="headline-light" x="605" y="972">what's your</text>
    <text class="headline-house" x="606" y="1090">House</text>
    <text class="headline-worth" x="606" y="1166">IS WORTH</text>
  </g>

  <g class="cta-block">
    <text class="cta" x="38" y="1142">Call</text>
    <text class="cta" x="38" y="1190">us</text>
    <text class="cta" x="38" y="1243">Today</text>
    <circle cx="270" cy="1287" r="25" fill="var(--white)"/>
    <path d="M6.6 10.8c1.4 2.8 3.8 5.1 6.6 6.6l2.2-2.2c.3-.3.7-.4 1-.2 1.1.4 2.3.6 3.6.6.6 0 1 .4 1 1V20c0 .6-.4 1-1 1C10.6 21 3 13.4 3 4c0-.6.4-1 1-1h3.5c.6 0 1 .4 1 1 0 1.3.2 2.5.6 3.6.1.3 0 .7-.2 1L6.6 10.8z" fill="var(--navy)" transform="translate(256 1273) scale(1.15)"/>
    <text class="cta-phone" x="326" y="1302">+61 3555 0142</text>
  </g>
</svg>

<!-- Back side -->
<svg class="flyer flyer--back" viewBox="0 0 633 1343" xmlns="http://www.w3.org/2000/svg">
  <defs>
    <linearGradient id="back-red" x1="0" y1="0" x2="1" y2="0">
      <stop offset="0" stop-color="var(--red-dark)"/>
      <stop offset="1" stop-color="var(--red)"/>
    </linearGradient>
    <linearGradient id="portrait-tone" x1="0" y1="0" x2="0" y2="1">
      <stop offset="0" stop-color="#8c8582"/>
      <stop offset="1" stop-color="#5c5552"/>
    </linearGradient>
    <clipPath id="portrait-clip">
      <circle cx="315" cy="528" r="135"/>
    </clipPath>
  </defs>

  <rect class="flyer-bg" width="633" height="1343" fill="url(#back-red)"/>
  <path class="navy-panel" d="M0 251 L190 61 Q205 46 232 46 L633 46 L633 916 L340 1209 Q310 1239 278 1239 L0 1239 Z" fill="var(--navy)"/>

  <g class="tagline-block" text-anchor="middle">
    <text class="tagline" x="317" y="220">Where a Dream</text>
    <text class="tagline" x="317" y="274">Come Home</text>
  </g>

  <g class="agent-portrait">
    <circle cx="315" cy="528" r="135" fill="var(--yellow)"/>
    <rect role="img" aria-label="Portrait of the agent in a suit" x="195" y="420" width="240" height="260" rx="60" fill="url(#portrait-tone)" clip-path="url(#portrait-clip)"/>
  </g>

  <g class="agent-info" text-anchor="middle">
    <text class="agent-name" x="317" y="757">Rohan Mehta</text>
    <text class="agent-role" x="317" y="792">Managing Director/LEA, Meridian Realty</text>
  </g>

  <line class="divider" x1="48" y1="835" x2="586" y2="835" stroke="var(--yellow)" stroke-width="1.5"/>

  <g class="contact-list">
    <path d="M6.6 10.8c1.4 2.8 3.8 5.1 6.6 6.6l2.2-2.2c.3-.3.7-.4 1-.2 1.1.4 2.3.6 3.6.6.6 0 1 .4 1 1V20c0 .6-.4 1-1 1C10.6 21 3 13.4 3 4c0-.6.4-1 1-1h3.5c.6 0 1 .4 1 1 0 1.3.2 2.5.6 3.6.1.3 0 .7-.2 1L6.6 10.8z" fill="var(--yellow)" transform="translate(108 898) scale(0.85)"/>
    <text class="contact" x="151" y="918">03 5550 1234</text>

    <rect x="370" y="896" width="13" height="24" rx="2.5" fill="none" stroke="var(--yellow)" stroke-width="2.5"/>
    <text class="contact" x="402" y="918">0400 555 012</text>

    <path d="M120 940 a8 8 0 0 1 8 8 c0 6-8 14-8 14 s-8-8-8-14 a8 8 0 0 1 8-8z" fill="var(--yellow)"/>
    <circle cx="120" cy="948" r="3" fill="var(--navy)"/>
    <text class="contact" x="152" y="963">14/8 Harbour Lane</text>
    <text class="contact" x="152" y="986">Westvale 3030</text>

    <g fill="none" stroke="var(--yellow)" stroke-width="2">
      <circle cx="119" cy="1022" r="10"/>
      <ellipse cx="119" cy="1022" rx="4.5" ry="10"/>
      <line x1="109" y1="1022" x2="129" y2="1022"/>
      <line x1="111" y1="1016" x2="127" y2="1016"/>
      <line x1="111" y1="1028" x2="127" y2="1028"/>
    </g>
    <text class="contact" x="152" y="1029">www.meridianrealty.com.au</text>

    <rect x="109" y="1062" width="20" height="14" fill="var(--yellow)"/>
    <path d="M109 1062 L119 1070 L129 1062" fill="none" stroke="var(--navy)" stroke-width="1.8"/>
    <text class="contact" x="152" y="1075">rohan@meridianrealty.com.au</text>
  </g>

  <g class="brand">
    <rect x="392" y="1238" width="46" height="46" rx="6" fill="var(--navy)"/>
    <text class="brand-name brand-name--light" x="448" y="1274">meridian</text>
  </g>
</svg>

</body>
</html>
```